Bref créative
Bridgewell Brochure
Brochure
The brochure I want is a double-sided, tri-fold, 8.5" x 11". I have uploaded a sketch on what I would like on each side, as well as my original brochure. I will describe what I want on each side, and each section.
Inside (refer to formatting of original brochure):
left -- I want this section to be very similar to the original, but with a new design consistent with our colors and logo. Attached is a file titled "Bridgewell Brochure -- NEW TEXT" that is the new text I want in the section.
middle -- I want the text of the original brochure to remain the same, but consistent with new design/colors, and also if we can use our logo's "cube" as the new separator between the testimonials.
right -- I want this to be all new (not like original), with the text, "Visit us on the web at: www.BridgewellHoldingsNY.example" and below that, the text, "find our Attorney tab". The designer is open to design this section any way they would like, consistent with the overall design.
Outside (refer to formatting of original brochure):
left -- this section can be just like the original brochure, just with the updated design. I still want 'scales of justice' included in this section.
middle -- same as original brochure, just with our new address: 418 Maplecrest Avenue, Floral Park, NY 11001
right -- same as original brochure, just with new design
On the whole, I am looking for a design that is a little more sleek, modern, and simple. I would urge the designers to please stay away from swirly text or design features.
Real Estate
attorneys and businessmen
I have uploaded both sides of our old brochure. We want something nearly identical, just more reflective of our colors and style.
I have also uploaded our logo, business card, and new text for the left side of the inside of the brochure.
Lastly, I am uploading a new mock-up of the 6 sections of the brochure (similar to old version).
ANY SUBMISSION THAT DEVIATES TOO MUCH FROM OUR PREVIOUS DESIGN WILL BE IMMEDIATELY ELIMINATED.

```html
<!DOCTYPE html>
<html lang="en">
<head>
<meta charset="utf-8">
<title>Bridgewell Asset Management – Tri-fold Brochure</title>
<link href="https://fonts.googleapis.com/css2?family=Crimson+Text:ital,wght@0,400;0,600;0,700;1,400&display=swap" rel="stylesheet">
<style>
  :root {
    --bg: #e8e5e0;
    --paper: #ffffff;
    --paper-shade: #f3f3f5;
    --gold: #c99a2e;
    --gold-dark: #a87a18;
    --purple: #3d3585;
    --purple-dark: #2a2468;
    --ink: #55555f;
    --rule: #d9d9de;
  }
  * { box-sizing: border-box; margin: 0; padding: 0; }
  html, body { width: 1200px; height: 897px; overflow: hidden; }
  body {
    background: var(--bg);
    font-family: "Crimson Text", serif;
    color: var(--ink);
    position: relative;
    font-variant-ligatures: none;
  }
  h2 { font-weight: 400; }
  .sheet {
    position: absolute;
    background: var(--paper);
    display: flex;
    box-shadow: 0 2px 8px rgba(0,0,0,.15);
  }
  .sheet--outside { left: 48px; top: 24px; width: 558px; height: 441px; }
  .sheet--inside  { left: 48px; top: 490px; width: 558px; height: 388px; }
  .panel {
    position: relative;
    width: 186px;
    height: 100%;
    border-right: 1px solid var(--rule);
    overflow: hidden;
  }
  .panel:last-child { border-right: 0; }

  /* Outside – offering panel */
  .offering-head {
    background: linear-gradient(var(--paper-shade), #fff);
    padding: 10px 14px 6px;
    font-size: 22px;
    color: var(--purple);
    border-bottom: 2px dotted var(--gold);
  }
  .offering-list { list-style: none; padding: 12px 14px 0; }
  .offering-list li {
    display: flex; align-items: center; gap: 7px;
    font-size: 10px; color: var(--purple); margin-bottom: 9px;
  }
  .offering-list li::before {
    content: ""; width: 8px; height: 8px; border-radius: 50%;
    background: var(--purple); flex: none;
  }
  .scales-art {
    margin: 8px 26px 0;
    height: 130px;
    background: radial-gradient(circle at 50% 50%, #e2b451, #a8781a 70%, #fff 71%);
  }
  .toll-free {
    position: absolute; left: 14px; bottom: 28px;
    color: var(--purple); font-size: 12px; line-height: 1.15;
  }
  .toll-free strong { display: block; font-size: 17px; font-weight: 600; }

  /* Outside – mailing panel */
  .return-address {
    position: absolute; right: 8px; top: 10px;
    writing-mode: vertical-rl;
    font-size: 7.5px; line-height: 1.4; color: var(--ink);
  }
  .faint-block {
    position: absolute; background: #eceef2; opacity: .7;
  }

  /* Cover */
  .cover { background: linear-gradient(90deg, #fff, var(--paper-shade)); }
  .cover-band {
    position: absolute; left: 0; top: 0; bottom: 0; width: 30px;
    background: linear-gradient(90deg, var(--gold-dark), var(--gold) 60%, #e4bf63);
  }
  .cover-band--purple { background: linear-gradient(90deg, var(--purple-dark), var(--purple) 60%, #6760a8); }
  .cover-title {
    position: absolute; left: 36px; right: 10px; top: 48px;
    color: var(--purple); font-size: 20px; line-height: 1.08;
  }
  .dotted { border-top: 2px dotted var(--gold); }
  .cover-rule-top { position: absolute; left: 36px; right: 10px; top: 150px; }
  .cover-rule-bottom { position: absolute; left: 36px; right: 10px; top: 250px; }
  .brand {
    position: absolute; left: 36px; right: 10px; top: 184px;
    display: flex; flex-direction: column; align-items: center; gap: 3px;
  }
  .brand-mark { width: 22px; height: 22px; background: var(--purple); }
  .brand-name {
    display: flex; flex-direction: column; align-items: center;
    color: var(--purple); font-weight: 600;
    text-transform: uppercase; text-align: center; line-height: 1.05;
    white-space: nowrap;
  }
  .brand-name__main { font-size: 15px; letter-spacing: .5px; }
  .brand-name__sub { font-size: 8.5px; letter-spacing: .4px; }

  /* Inside */
  .inside-panel { padding: 12px 12px 0; }
  .inside-head {
    color: var(--purple); font-size: 17px; line-height: 1.05;
    padding-bottom: 5px; border-bottom: 2px dotted var(--gold); margin-bottom: 7px;
  }
  .inside-head--second { margin-top: 12px; }
  .body-text { font-size: 8px; line-height: 1.35; margin-bottom: 6px; }
  .subhead { font-size: 8px; font-weight: 700; color: var(--ink); margin-bottom: 6px; }
  .lead-italic { font-size: 8px; font-style: italic; margin-bottom: 6px; }
  .testimonial { margin-bottom: 6px; }
  .testimonial cite { display: block; font-size: 7px; font-style: normal; color: var(--purple); margin-top: 2px; }
  .separator { width: 11px; height: 11px; background: var(--gold); margin: 4px 0 6px; }
  .web-cta {
    position: absolute; left: 0; right: 0; bottom: 16px;
    text-align: center; color: var(--purple); font-size: 9px; line-height: 1.3;
  }
  .web-cta strong { display: block; font-weight: 700; font-size: 8.5px; }

  /* Standalone cover variants */
  .cover-card {
    position: absolute; top: 36px; width: 220px; height: 455px;
    background: linear-gradient(90deg, #fff, var(--paper-shade));
    box-shadow: 0 2px 8px rgba(0,0,0,.15);
    overflow: hidden;
  }
  .cover-card--gold { left: 640px; }
  .cover-card--purple { left: 890px; }
  .cover-card .cover-band { width: 36px; }
  .cover-card .cover-title { left: 46px; top: 60px; font-size: 24px; }
  .cover-card .cover-rule-top { left: 46px; top: 186px; }
  .cover-card .brand { left: 46px; top: 222px; }
  .cover-card .brand-mark { width: 26px; height: 26px; }
  .cover-card .brand-name__main { font-size: 18px; }
  .cover-card .brand-name__sub { font-size: 10px; }
  .cover-card .cover-rule-bottom { left: 46px; top: 302px; }
</style>
</head>
<body>

<!-- Outside spread -->
<section class="sheet sheet--outside" aria-label="Brochure outside">
  <div class="panel">
    <h2 class="offering-head">Offering</h2>
    <ul class="offering-list">
      <li>Prompt Professional Service</li>
      <li>Immediate Closings</li>
      <li>All Cash purchases</li>
      <li>Honesty and Integrity</li>
    </ul>
    <div class="scales-art" role="img" aria-label="Gold scales of justice illustration"></div>
    <p class="toll-free">Toll Free<strong>1-800-555-0142</strong></p>
  </div>

  <div class="panel">
    <p class="return-address">Bridgewell Asset Management<br>418 Maplecrest Avenue, Floral Park, NY 11001</p>
    <div class="faint-block" style="left:40px;top:250px;width:90px;height:90px;"></div>
    <div class="faint-block" style="left:70px;top:330px;width:70px;height:70px;"></div>
  </div>

  <div class="panel cover">
    <div class="cover-band"></div>
    <p class="cover-title">Providing Solutions For You &amp; Your Clients</p>
    <div class="dotted cover-rule-top"></div>
    <div class="brand">
      <span class="brand-mark"></span>
      <span class="brand-name"><span class="brand-name__main">Bridgewell</span><span class="brand-name__sub">Asset Management</span></span>
    </div>
    <div class="dotted cover-rule-bottom"></div>
  </div>
</section>

<!-- Inside spread -->
<section class="sheet sheet--inside" aria-label="Brochure inside">
  <div class="panel inside-panel">
    <h2 class="inside-head">The name you<br>can trust</h2>
    <p class="body-text">Bridgewell Asset Management was founded to give attorneys and their clients a dependable partner for real estate matters. We purchase residential property quickly and fairly, and we handle every step with care.</p>
    <p class="body-text">Our team works closely with counsel, executors and families to reach a settlement that suits everyone involved.</p>
    <h2 class="inside-head inside-head--second">When a swift closing<br>is desired...</h2>
    <p class="body-text">Our funds are ready when you are. We can close within days, pay all cash and take the property as it stands.</p>
    <p class="body-text">Bridgewell Asset Management keeps each transaction simple, clear and on schedule.</p>
  </div>

  <div class="panel inside-panel">
    <h2 class="inside-head">Don't just take our<br>word for it...</h2>
    <p class="lead-italic">Hear what our colleagues have to say!</p>
    <blockquote class="testimonial">
      <p class="body-text">"Their team made a difficult estate sale simple. The closing was fast and every detail was handled."</p>
      <cite>Martin Ellery, Esq. · Estate Attorney</cite>
    </blockquote>
    <div class="separator"></div>
    <blockquote class="testimonial">
      <p class="body-text">"I refer my clients with confidence. They are honest, prompt and easy to work with."</p>
      <cite>Dana Whitlow, Esq. · Probate Counsel</cite>
    </blockquote>
    <div class="separator"></div>
    <blockquote class="testimonial">
      <p class="body-text">"A reliable partner for any closing. I would gladly recommend them to colleagues."</p>
      <cite>Paul Renner · Broker</cite>
    </blockquote>
  </div>

  <div class="panel inside-panel">
    <h2 class="inside-head">Find our attorney</h2>
    <p class="subhead">Providing Solutions for You and Your Clients</p>
    <p class="body-text">Bridgewell Asset Management maintains a list of trusted attorneys who assist with contracts, title review and closings.</p>
    <p class="body-text">To find counsel near you, visit our website and open the attorney section for names and contact details.</p>
    <div class="faint-block" style="left:60px;top:200px;width:80px;height:80px;"></div>
    <p class="web-cta">Visit us at<strong>www.BridgewellHoldingsNY.example</strong></p>
  </div>
</section>

<!-- Cover variants -->
<section class="cover-card cover-card--gold" aria-label="Cover, gold variant">
  <div class="cover-band"></div>
  <p class="cover-title">Providing Solutions For You &amp; Your Clients</p>
  <div class="dotted cover-rule-top"></div>
  <div class="brand">
    <span class="brand-mark"></span>
    <span class="brand-name"><span class="brand-name__main">Bridgewell</span><span class="brand-name__sub">Asset Management</span></span>
  </div>
  <div class="dotted cover-rule-bottom"></div>
</section>

<section class="cover-card cover-card--purple" aria-label="Cover, purple variant">
  <div class="cover-band cover-band--purple"></div>
  <p class="cover-title">Providing Solutions For You &amp; Your Clients</p>
  <div class="dotted cover-rule-top"></div>
  <div class="brand">
    <span class="brand-mark"></span>
    <span class="brand-name"><span class="brand-name__main">Bridgewell</span><span class="brand-name__sub">Asset Management</span></span>
  </div>
  <div class="dotted cover-rule-bottom"></div>
</section>

</body>
</html>
```